Civil engineering company | Billboard

We need a billboard design for Velmora- civil engineering company. We want big logo in the center of billboard and web site (www.velmora.hr) below the logo. Also, we want an subtle abstract pattern in the background. Dimensions of the billboard are: width :10 m, height: 2m. Design must be celan and modern.
Industry/Entity Type
Civil engineering
Font styles to use
Sans Serif
Colors
F0912C
F2A743
F7CA91
FBE8D2
FDF5EE
Requirements
Must have
- Logo and new unique pattern design for Velmroa company
Should not have
- pictures of construction machinery and tools

```html
<!DOCTYPE html>
<html lang="hr">
<head>
<meta charset="utf-8">
<title>Velmora – billboard</title>
<link href="https://fonts.googleapis.com/css2?family=Montserrat:wght@300;500;600&display=swap" rel="stylesheet">
<style>
  :root {
    --stage: #e6e4e1;
    --board: #222224;
    --board-deep: #1a1a1b;
    --orange: #F0912C;
    --orange-mid: #F2A743;
    --orange-light: #F7CA91;
    --cream: #FBE8D2;
    --text-light: #e2e2e2;
  }
  html, body {
    margin: 0;
    padding: 0;
    width: 1200px;
    height: 1040px;
    overflow: hidden;
    background: var(--stage);
  }
  .canvas {
    position: relative;
    width: 1200px;
    height: 1040px;
  }
  .billboard {
    position: absolute;
    left: 0;
    top: 400px;
    width: 1200px;
    height: 240px;
    display: block;
  }
  .brand-name {
    font-family: "Montserrat", sans-serif;
    font-weight: 500;
    fill: var(--orange);
  }
  .tagline {
    font-family: "Montserrat", sans-serif;
    font-weight: 600;
    fill: var(--text-light);
  }
  .website {
    font-family: "Montserrat", sans-serif;
    font-weight: 300;
    fill: var(--text-light);
  }
</style>
</head>
<body>
<div class="canvas">
  <svg class="billboard" viewBox="0 0 1200 240" xmlns="http://www.w3.org/2000/svg">
    <defs>
      <linearGradient id="chevron-left-fill" x1="0" y1="0" x2="1" y2="0">
        <stop offset="0" stop-color="var(--orange-light)"/>
        <stop offset="1" stop-color="var(--orange)"/>
      </linearGradient>
      <linearGradient id="chevron-right-fill" x1="1" y1="0" x2="0" y2="0">
        <stop offset="0" stop-color="var(--orange-light)"/>
        <stop offset="1" stop-color="var(--orange)"/>
      </linearGradient>
      <radialGradient id="dot-field" cx="0.5" cy="0.5" r="0.5">
        <stop offset="0" stop-color="#5a5a5c" stop-opacity="0.55"/>
        <stop offset="1" stop-color="#5a5a5c" stop-opacity="0"/>
      </radialGradient>
    </defs>

    <rect class="board-base" width="1200" height="240" fill="var(--board)"/>

    <!-- halftone fields -->
    <rect class="dot-pattern" role="img" aria-label="Subtle halftone dot pattern" x="60" y="0" width="150" height="240" fill="url(#dot-field)"/>
    <rect class="dot-pattern" role="img" aria-label="Subtle halftone dot pattern" x="990" y="0" width="150" height="240" fill="url(#dot-field)"/>

    <!-- left chevron -->
    <path class="chevron-shadow" d="M0,-10 L150,108 Q165,120 150,132 L0,250 Z" fill="var(--board-deep)"/>
    <polygon class="chevron chevron--left" points="0,-10 142,120 0,250 0,196 95,120 0,44" fill="url(#chevron-left-fill)"/>

    <!-- right chevron -->
    <path class="chevron-shadow" d="M1200,-10 L1050,108 Q1035,120 1050,132 L1200,250 Z" fill="var(--board-deep)"/>
    <polygon class="chevron chevron--right" points="1200,-10 1058,120 1200,250 1200,196 1105,120 1200,44" fill="url(#chevron-right-fill)"/>

    <!-- brand block -->
    <rect class="brand-square" x="230" y="36" width="119" height="119" fill="none" stroke="var(--text-light)" stroke-width="2.5"/>
    <text class="brand-name" x="366" y="123" font-size="82" letter-spacing="1">VELMORA</text>
    <text class="tagline" x="369" y="152" font-size="20.5" textLength="601" lengthAdjust="spacingAndGlyphs">IZVOĐENJE I VOĐENJE GRAĐEVINSKIH RADOVA</text>

    <!-- website -->
    <g class="globe-icon" fill="none" stroke="var(--orange)" stroke-width="1.4" transform="translate(457 193)">
      <circle r="10"/>
      <ellipse rx="4.5" ry="10"/>
      <line x1="-10" y1="0" x2="10" y2="0"/>
      <line x1="-8.5" y1="-5" x2="8.5" y2="-5"/>
      <line x1="-8.5" y1="5" x2="8.5" y2="5"/>
      <line x1="0" y1="-10" x2="0" y2="10"/>
    </g>
    <line class="website-divider" x1="476" y1="176" x2="476" y2="211" stroke="var(--orange)" stroke-width="1.4"/>
    <text class="website" x="483" y="203" font-size="27">www.velmora.hr</text>
  </svg>
</div>
</body>
</html>
```